QUOTE Graphics for Summer Challenge

I would like to put these quotes over one of the pictures attached; For Instagram, use new size: 4:5 (1080 x 1350 pixels). One Quote per picture, and I want the quote to be bold or easy to read as well. I provided a few reference graphics that I really like as examples below.
All of the pictures are attached; you can pick any photo and add one quote to it; but no stock photography
All the quotes are in the attached WORD document

```html
<!DOCTYPE html>
<html lang="en">
<head>
<meta charset="UTF-8">
<title>Hot Girl Summer Slimdown</title>
<link rel="stylesheet" href="https://fonts.googleapis.com/css2?family=Roboto+Condensed:wght@700&display=swap">
<style>
  :root {
    --sky: #8fc6e6;
    --hills: #8a9a7a;
    --pool: #5fc4dc;
    --pool-light: #bfe6ef;
    --edge-violet: #5a4f86;
    --panel-top-a: rgba(214, 84, 130, 0.86);
    --panel-top-b: rgba(200, 70, 120, 0.9);
    --panel-bottom: rgba(236, 108, 128, 0.92);
    --text: #ffffff;
  }
  html, body {
    margin: 0;
    padding: 0;
    width: 960px;
    height: 1200px;
    overflow: hidden;
  }
  .post {
    position: relative;
    width: 960px;
    height: 1200px;
    overflow: hidden;
    font-family: "Roboto Condensed", "Arial Narrow", sans-serif;
  }
  .post-photo {
    position: absolute;
    inset: 0;
    background:
      linear-gradient(90deg, rgba(0,0,0,0) 88%, var(--edge-violet) 100%),
      linear-gradient(180deg, var(--sky) 0%, #b8d8ea 22%, var(--hills) 30%, #9aa98a 42%, var(--pool) 47%, #7dd0e2 75%, var(--pool-light) 100%);
  }
  .quote-panel {
    position: absolute;
    left: 345px;
    width: 579px;
    top: 0;
    height: 1200px;
  }
  .quote-panel__main {
    position: absolute;
    inset: 0 0 357px 0;
    background: linear-gradient(160deg, var(--panel-top-a) 0%, var(--panel-top-b) 60%, rgba(222, 92, 130, 0.9) 100%);
  }
  .quote-panel__cta {
    position: absolute;
    left: 0;
    right: 0;
    bottom: 0;
    height: 357px;
    background: var(--panel-bottom);
  }
  .quote-text,
  .cta-text {
    position: absolute;
    left: 0;
    right: 0;
    margin: 0;
    color: var(--text);
    text-align: center;
    text-transform: uppercase;
    font-weight: 700;
    font-size: 80px;
    line-height: 73px;
    letter-spacing: 2px;
  }
  .quote-text { top: 140px; }
  .cta-text { top: 870px; }
</style>
</head>
<body>
  <main class="post">
    <div class="post-photo" role="img" aria-label="Photo of a woman in a black bikini stepping out of an infinity pool, hills and blue sky behind her"></div>
    <section class="quote-panel">
      <div class="quote-panel__main"></div>
      <div class="quote-panel__cta"></div>
      <h1 class="quote-text">This hot girl<br>summer<br>slimdown<br>plan is<br>helping<br>women drop<br>pounds and<br>feel sexy<br>again.</h1>
      <p class="cta-text">Comment<br>summer to<br>join us</p>
    </section>
  </main>
</body>
</html>
```